Design cover for information booklet
I am looking for a design for the front and back cover of an information booklet. Also an inside page basic design.
The booklet will contain 10 double sided pages providing information on weight loss surgery.
See my website www.bernardpaxley.com.au for what I do and typical colour themes.
I would also like some theming/illustration which can be utilised on each inside page of the booklet, rather than the pages just being blank with text etc. What would a blank page on this inside of the booklet look like under the design theme that you have created?
My company is Harrowgate Institute for Metabolic Surgery. You will find uploaded a Logo for Harrowgate Institute for Metabolic Surgery as well as my other logo which is my name “Bernard Paxley, etc.”. The Harrowgate Institute for Metabolic Surgery logo should be utilised. The other logo (Bernard Paxley) is optional.
The front cover should contain the following text as minimum:
Harrowgate Institute for Metabolic Surgery
Mr Bernard Paxley MBBS FRACS GradCert (Health Stats)
Our tagline is “Experience, Expertise and Empathy”. This should probably be on the front cover also.
The back cover contains (as a minimum) our address, phone number, fax number:
Suite 47, Level 3
Wrenfield Valley Hospital
14 Dunmore Lane, Glenrock VIC 3291
Phone: 03 9461 3087
Fax: 03 9462 5518
Email: info@harrowgateims.com.au
The files should be in a form whereby the text can be edited and changed if need be.
1. problems with initial graphical attachments - Artquorum end 2. several requests by designers for extension

```html
<!DOCTYPE html>
<html lang="en">
<head>
<meta charset="utf-8">
<title>Harrowgate Institute – Booklet Covers and Inside Page</title>
<link rel="stylesheet" href="https://fonts.googleapis.com/css2?family=Oswald:wght@300;500;700&family=Open+Sans:wght@400;600&family=Cinzel:wght@500&display=swap">
<style>
  :root {
    --stage: #0aaa9f;
    --page: #ffffff;
    --teal-dark: #17695f;
    --teal: #1f7d71;
    --teal-light: #2a8a7d;
    --ink: #2b2b2b;
    --muted: #9a9a9a;
  }
  * { margin: 0; padding: 0; box-sizing: border-box; }
  html, body { width: 1200px; height: 1200px; overflow: hidden; }
  body {
    background: var(--stage);
    position: relative;
    font-family: "Open Sans", Arial, sans-serif;
  }
  .page {
    position: absolute;
    width: 377px;
    height: 529px;
    background: var(--page);
    box-shadow: 0 6px 22px rgba(0,0,0,.25);
    overflow: hidden;
  }
  .front-cover { left: 187px; top: 53px; }
  .back-cover  { left: 636px; top: 53px; }
  .inside-page { left: 414px; top: 619px; }

  /* Front cover */
  .brand-mark {
    position: absolute;
    display: flex;
    align-items: center;
    gap: 6px;
    font-family: "Cinzel", Georgia, serif;
    font-weight: 500;
    color: var(--teal);
  }
  .brand-mark .square {
    width: 24px; height: 24px;
    background: var(--teal);
    flex: none;
  }
  .front-cover .brand-mark {
    left: 124px; top: 17px;
    width: 140px;
    font-size: 9px;
    line-height: 1.15;
  }
  .headline {
    position: absolute;
    left: 130px; top: 80px;
    font-family: "Oswald", sans-serif;
    font-weight: 700;
    font-size: 47px;
    line-height: 1;
    color: var(--teal);
    letter-spacing: .2px;
  }
  .subline {
    position: absolute;
    left: 55px; top: 133px;
    font-family: "Oswald", sans-serif;
    font-weight: 300;
    font-size: 21px;
    line-height: 1;
    color: var(--ink);
  }
  .cover-band {
    position: absolute;
    left: 0; top: 210px;
    width: 377px; height: 108px;
  }
  .web-address {
    position: absolute;
    left: 0; right: 0; top: 505px;
    text-align: center;
    font-size: 7px;
    color: var(--teal);
  }

  /* Back cover */
  .chevron-band {
    position: absolute;
    left: 0; top: 206px;
    width: 377px; height: 116px;
  }
  .back-cover .brand-mark {
    left: 0; right: 0; top: 222px;
    flex-direction: column;
    gap: 4px;
    color: #ffffff;
    font-size: 6px;
    text-align: center;
  }
  .back-cover .brand-mark .square {
    width: 38px; height: 38px;
    background: none;
    border: 3px solid #ffffff;
  }
  .contact {
    position: absolute;
    top: 283px;
    font-size: 5.4px;
    line-height: 8.4px;
    color: #e6f2f0;
  }
  .contact-address { left: 140px; display: flex; gap: 6px; align-items: flex-start; }
  .contact-lines { left: 250px; }
  .contact-lines li { list-style: none; display: flex; align-items: center; gap: 6px; }
  .contact svg { flex: none; }
  .signature-name {
    position: absolute;
    left: 127px; top: 490px;
    display: flex; align-items: center; gap: 5px;
    font-family: "Cinzel", Georgia, serif;
    font-weight: 500;
    font-size: 11px;
    color: var(--teal);
  }
  .signature-name .dot {
    width: 20px; height: 20px; border-radius: 50%;
    background: var(--teal);
  }

  /* Inside page */
  .top-rule {
    position: absolute;
    left: 0; top: 16px;
    width: 86px; height: 7px;
    background: var(--teal);
  }
  .page-number {
    position: absolute;
    left: 352px; top: 15px;
    font-size: 6px;
    color: var(--muted);
  }
  .inside-page .signature-name { left: 18px; top: 488px; }
  .page-illustration {
    position: absolute;
    left: 307px; top: 472px;
    width: 54px; height: 38px;
    background: linear-gradient(180deg, #f2c7a8 0%, #7fc6d8 55%, #2d7f92 100%);
    border-radius: 3px;
  }
</style>
</head>
<body>

  <section class="page front-cover">
    <div class="brand-mark"><span class="square"></span><span>Harrowgate Institute for Metabolic Surgery</span></div>
    <h1 class="headline">EXPERIENCE</h1>
    <p class="subline">EXPERTISE AND EMPATHY</p>
    <svg class="cover-band" viewBox="0 0 377 108" role="img" aria-label="Photograph of surgeons operating in a theatre beneath surgical lights">
      <defs>
        <linearGradient id="theatre" x1="0" y1="0" x2="1" y2="0">
          <stop offset="0" stop-color="#3f6f6a"/>
          <stop offset=".45" stop-color="#c9d3d4"/>
          <stop offset=".8" stop-color="#9fb3bd"/>
          <stop offset="1" stop-color="#6b8594"/>
        </linearGradient>
      </defs>
      <rect width="377" height="108" fill="url(#theatre)"/>
      <polygon points="0,0 72,0 126,54 72,108 0,108" fill="var(--teal-dark)"/>
      <polygon points="72,0 126,54 72,108 18,54" fill="var(--teal)" opacity=".55"/>
    </svg>
    <p class="web-address">www.bernardpaxley.com.au</p>
  </section>

  <section class="page back-cover">
    <svg class="chevron-band" viewBox="0 0 377 116" aria-hidden="true">
      <polygon points="20,58 85,0 377,0 377,116 85,116" fill="var(--teal-dark)"/>
      <polygon points="45,58 110,0 377,0 377,116 110,116" fill="var(--teal)"/>
    </svg>
    <div class="brand-mark"><span class="square"></span><span>Harrowgate Institute</span></div>
    <div class="contact contact-address">
      <svg width="6" height="8" viewBox="0 0 6 8"><path d="M3 0a3 3 0 0 0-3 3c0 2.2 3 5 3 5s3-2.8 3-5a3 3 0 0 0-3-3zm0 4.2a1.2 1.2 0 1 1 0-2.4 1.2 1.2 0 0 1 0 2.4z" fill="#fff"/></svg>
      <p>Suite 47, Level 3<br>Wrenfield Valley Hospital<br>14 Dunmore Lane, Glenrock VIC 3291</p>
    </div>
    <ul class="contact contact-lines">
      <li><svg width="6" height="6" viewBox="0 0 6 6"><path d="M1.2 0l1 1.4-.6.8a3.5 3.5 0 0 0 2.2 2.2l.8-.6L6 4.8 5.2 6C2.4 6 0 3.6 0 .8z" fill="#fff"/></svg>03 9461 3087</li>
      <li><svg width="6" height="6" viewBox="0 0 6 6"><rect x="0" y="2" width="6" height="3.5" fill="#fff"/><rect x="1.5" y="0" width="3" height="2" fill="#fff"/></svg>03 9462 5518</li>
      <li><svg width="6" height="5" viewBox="0 0 6 5"><rect width="6" height="5" fill="#fff"/><path d="M0 0l3 2.6L6 0" stroke="var(--teal)" stroke-width=".7" fill="none"/></svg>info@harrowgateims.com.au</li>
    </ul>
    <div class="signature-name"><span class="dot"></span><span>Bernard Paxley</span></div>
  </section>

  <section class="page inside-page">
    <div class="top-rule"></div>
    <span class="page-number">01</span>
    <div class="signature-name"><span class="dot"></span><span>Bernard Paxley</span></div>
    <div class="page-illustration" role="img" aria-label="Small illustration of a surgical team around an operating table"></div>
  </section>

</body>
</html>
```